Loomtide - agency page

We are a full service digital agency. Design, development, marketing and SEO/content - but we haven’t got time for our own page. Site looks now like a one pager with just text. We want to keep the colors we got, and the logo stays the same. The site is https://loomtide.no. We need at least a frontpage and an article page. Archive is nice to have.

We are also need more designers for client projects, so there might be more work here.

```html
<!DOCTYPE html>
<html lang="en">
<head>
<meta charset="utf-8">
<title>Loomtide — Digital Agency</title>
<link rel="stylesheet" href="https://fonts.googleapis.com/css2?family=Young+Serif&family=Urbanist:wght@400;500;600;700&display=swap">
<style>
:root{
  --ink:#2b2a35;
  --muted:#6a6874;
  --lilac:#d6a5f4;
  --lilac-deep:#a95fd6;
  --accent:#c77ff0;
  --line:#bdbbc2;
  --soft:#efeef0;
  --card:#dedddf;
  --footer:#3b2a3a;
  --white:#ffffff;
}
*{box-sizing:border-box;margin:0;padding:0}
html,body{width:1200px;height:4375px;overflow:hidden}
body{position:relative;background:var(--white);color:var(--ink);font-family:"Urbanist",sans-serif}
.abs{position:absolute}
.serif{font-family:"Young Serif",serif;font-weight:400}
.btn{position:absolute;display:flex;align-items:center;justify-content:center;background:var(--lilac);border:1.5px solid var(--lilac-deep);border-radius:22px;box-shadow:2px 3px 0 #8e5ab0;font-size:13px;font-weight:600;color:var(--ink)}
.eyebrow{position:absolute;display:flex;align-items:center;gap:8px;color:var(--accent);font-size:12px;letter-spacing:.5px;text-transform:uppercase}
.eyebrow::before{content:"";width:32px;height:1.5px;background:var(--accent)}
/* brand name */
.brand-name{position:absolute;display:flex;align-items:center;gap:8px;font-weight:500;color:var(--ink)}
.brand-name::before{content:"";border-radius:50%;background:var(--accent)}
.brand-name--header{left:80px;top:42px;font-size:20px}
.brand-name--header::before{width:10px;height:10px}
.brand-name--footer{left:100px;top:135px;font-size:36px;color:var(--white);gap:12px}
.brand-name--footer::before{width:16px;height:16px}
/* header */
.header-rule{left:178px;top:54px;width:472px;height:1px;background:var(--line)}
.nav{position:absolute;left:678px;top:45px;display:flex;gap:22px;font-size:12px;font-weight:500}
/* hero */
.hero-title{left:80px;top:212px;font-size:44px;line-height:51px}
.hero-copy{left:80px;top:392px;width:460px;font-size:13px;line-height:21px;color:var(--muted)}
.watch{left:230px;top:488px;display:flex;align-items:center;gap:8px;font-size:13px;font-weight:500}
.hero-art{left:590px;top:180px;width:535px;height:365px;background:radial-gradient(ellipse at 55% 55%,#e0c2f3 0%,#ececf0 45%,#fff 75%)}
/* brands */
.trusted{left:0;width:1200px;top:673px;text-align:center;font-size:14px;color:#c3c2c7}
.brands{left:82px;top:734px;width:1030px;display:flex;justify-content:space-between;font-size:29px;font-weight:700;color:#bcbcc0}
/* services */
.section-title{left:0;width:1200px;text-align:center;font-size:43px}
.services-copy{left:115px;width:970px;top:1050px;text-align:center;font-size:13.5px;line-height:21px;color:var(--muted)}
.rule{left:80px;width:1040px;height:1.5px;background:var(--line)}
.service{position:absolute;left:98px;width:1002px;display:flex;align-items:center;height:50px}
.service .num{color:var(--accent);font-size:30px;font-weight:700;width:62px}
.service .name{font-size:36px;font-weight:500;flex:1}
.arrow-btn{width:50px;height:50px;border-radius:50%;background:var(--lilac);border:1.5px solid var(--lilac-deep);box-shadow:1px 3px 0 #8e5ab0;display:flex;align-items:center;justify-content:center}
.service-shot{left:100px;top:1303px;width:1000px;height:330px;border-radius:14px;background:linear-gradient(115deg,#6b5aa0 0%,#3f3275 45%,#5a4a99 70%,#3a2c66 100%)}
.service-text{left:168px;top:1748px;width:580px;font-size:16px;line-height:26px;color:var(--ink)}
.service-divider{left:788px;top:1740px;width:3px;height:100px;background:var(--lilac)}
.delivery{left:843px;top:1743px;font-size:28px;line-height:50px;font-weight:500}
/* achievements */
.achieve{left:0;top:2228px;width:1200px;height:672px;background:var(--soft);border-top-right-radius:90px}
.achieve-title{left:80px;top:2342px;font-size:42px;line-height:52px}
.achieve-rule{left:80px;top:2490px;width:377px;height:1.5px;background:var(--line)}
.achieve-copy{left:160px;top:2542px;width:420px;font-size:16px;line-height:26px;color:var(--muted)}
.stat{position:absolute;left:653px;width:466px;height:108px;background:var(--card);border-radius:10px;display:flex;align-items:center;padding-left:25px;gap:22px}
.stat b{display:block;font-size:23px;font-weight:700}
.stat span{font-size:16px;color:var(--muted)}
/* testimonial */
.quote-copy{left:160px;top:3188px;width:520px;font-size:13.5px;line-height:22.5px;color:var(--muted)}
.avatar{left:160px;top:3342px;width:70px;height:70px;border-radius:50%;background:linear-gradient(135deg,#8fa39a,#3d4b45)}
.client{left:250px;top:3350px;font-size:17px;font-weight:600}
.client small{display:block;font-size:14px;font-weight:400;color:var(--muted);margin-top:12px}
.tree-art{left:820px;top:3160px;width:245px;height:255px;background:radial-gradient(circle at 50% 40%,#e3c7f4 0%,#f4ecf8 50%,#fff 75%)}
/* contact */
.getintouch{left:123px;top:3618px;font-size:58px;line-height:71px}
.field{position:absolute;border-bottom:1.5px solid var(--line);font-size:14px;color:var(--muted);padding-bottom:8px}
/* footer */
.footer{left:0;top:4003px;width:1200px;height:372px;background:var(--footer);color:var(--white)}
.col{position:absolute;top:70px;font-size:16px}
.col h4{font-size:17px;font-weight:700;letter-spacing:.5px;margin-bottom:22px}
.col li{list-style:none;margin-bottom:12px;display:flex;align-items:center;gap:10px}
.social{display:flex;gap:14px;margin-top:6px}
.social i{width:28px;height:28px;border-radius:50%;background:var(--white);display:block}
.foot-rule{left:55px;top:4310px;width:1093px;height:1px;background:#8a7a88}
.foot-bottom{position:absolute;top:4336px;font-size:16px;color:var(--white)}
</style>
</head>
<body>

<header>
  <div class="brand-name brand-name--header">Loomtide</div>
  <div class="abs header-rule"></div>
  <nav class="nav"><span>Services</span><span>Testimonials</span><span>About us</span><span>Contact us</span></nav>
  <div class="btn" style="left:992px;top:34px;width:123px;height:36px">Get Started</div>
</header>

<section class="hero">
  <div class="eyebrow" style="left:80px;top:184px">Digital Agency</div>
  <h1 class="abs serif hero-title">Empower Your Brand's<br>Digital Presence With<br>Loomtide</h1>
  <p class="abs hero-copy">Whether you're a startup looking to make a splash or an established brand seeking to expand your digital footprint, we are dedicated to delivering exceptional services tailored to your specific goals</p>
  <div class="btn" style="left:80px;top:482px;width:124px;height:36px">Get Started</div>
  <div class="abs watch">
    <svg width="24" height="24" viewBox="0 0 24 24"><circle cx="12" cy="12" r="11" fill="none" stroke="#2b2a35" stroke-width="1.5"/><path d="M9.5 7.5v9l7-4.5z" fill="#2b2a35"/></svg>
    Watch Demo
  </div>
  <div class="abs hero-art" role="img" aria-label="Illustration of a team fitting giant puzzle pieces together"></div>
</section>

<section class="brands-row">
  <p class="abs trusted">Trusted by more than 600 brands</p>
  <div class="abs brands"><span>Nordvale</span><span>Pixelmoor</span><span>Quarrystone</span><span>Brightfold</span><span>Halvard</span><span>Kestrel</span></div>
</section>

<section class="services">
  <svg class="abs" style="left:555px;top:893px" width="90" height="104" viewBox="0 0 90 104"><path d="M45 1 89 26v52L45 103 1 78V26z" fill="none" stroke="#e2e1e5" stroke-width="1.5"/></svg>
  <h2 class="abs serif section-title" style="top:912px">Our Services</h2>
  <p class="abs services-copy">Our digital agency offers a diverse range of services to meet all your digital needs. We specialize in web design and development, creating visually stunning and user-friendly websites that leave a lasting impression. Our team of experts is skilled in crafting effective e-commerce solutions that drive sales and enhance the customer experience.</p>

  <div class="abs rule" style="top:1163px"></div>
  <div class="service" style="top:1186px"><span class="num">01</span><span class="name">UI/UX Design</span><span class="arrow-btn"><svg width="26" height="14" viewBox="0 0 26 14"><path d="M1 7h23M18 1l6 6-6 6" fill="none" stroke="#2b2a35" stroke-width="1.5"/></svg></span></div>
  <div class="abs rule" style="top:1260px"></div>

  <div class="abs service-shot" role="img" aria-label="Screenshot of a dark purple marketplace website for digital art"></div>

  <div class="service" style="top:1670px"><span class="num">02</span><span class="name" style="font-size:40px">Web Development</span></div>
  <div class="btn" style="left:964px;top:1673px;width:134px;height:38px">Get Started</div>
  <p class="abs service-text">Our digital agency offers a diverse range of services to meet all your digital needs. We specialize in web design and development, creating visually stunning and user-friendly websites that leave a lasting impression.</p>
  <div class="abs service-divider"></div>
  <div class="abs delivery">4 Weeks Delivery<br>Starting at 1000 $</div>

  <div class="abs rule" style="top:1880px"></div>
  <div class="service" style="top:1903px"><span class="num">03</span><span class="name">Search Engine Optimization</span><span class="arrow-btn"><svg width="26" height="14" viewBox="0 0 26 14"><path d="M1 7h23M18 1l6 6-6 6" fill="none" stroke="#2b2a35" stroke-width="1.5"/></svg></span></div>
  <div class="abs rule" style="top:1976px"></div>
  <div class="service" style="top:1999px"><span class="num">04</span><span class="name">Digital Marketing</span><span class="arrow-btn"><svg width="26" height="14" viewBox="0 0 26 14"><path d="M1 7h23M18 1l6 6-6 6" fill="none" stroke="#2b2a35" stroke-width="1.5"/></svg></span></div>
  <div class="abs rule" style="top:2073px"></div>
</section>

<section class="abs achieve"></section>
<div class="eyebrow" style="left:80px;top:2325px">Achievements</div>
<h2 class="abs serif achieve-title">Leading the way in<br>digital marketing</h2>
<div class="abs achieve-rule"></div>
<p class="abs achieve-copy">The achievements we've gotten so far with our clients, marketing promotes the product awareness to the customers. Specially by advertising and promoting programs consumers get the information about the company and the products.</p>

<div class="stat" style="top:2492px">
  <svg width="56" height="56" viewBox="0 0 56 56" fill="none" stroke="#2b2a35" stroke-width="1.8"><circle cx="28" cy="28" r="26"/><ellipse cx="28" cy="28" rx="12" ry="26"/><path d="M2 28h52M6 15h44M6 41h44"/></svg>
  <div><b>120 +</b><span>Countries served in the world</span></div>
</div>
<div class="stat" style="top:2617px">
  <svg width="56" height="56" viewBox="0 0 56 56" fill="none" stroke="#2b2a35" stroke-width="1.8"><path d="M4 52h48M8 52V40h8v12M22 52V32h8v12M36 52V24h8v28M6 34 24 20l8 6 18-18M42 8h8v8"/></svg>
  <div><b>180 %</b><span>Average annual growth rate</span></div>
</div>
<div class="stat" style="top:2741px">
  <svg width="56" height="56" viewBox="0 0 56 56" fill="none" stroke="#2b2a35" stroke-width="1.8"><ellipse cx="28" cy="14" rx="22" ry="7"/><path d="M6 14v10c0 4 10 7 22 7s22-3 22-7V14M6 24v10c0 4 10 7 22 7s22-3 22-7V24M6 34v10c0 4 10 7 22 7s22-3 22-7V34"/></svg>
  <div><b>$ 420K</b><span>Sales made with the help of loomtide</span></div>
</div>

<section class="testimonials">
  <h2 class="abs serif section-title" style="top:3040px">Words from our happy clients</h2>
  <svg class="abs" style="left:85px;top:3195px" width="52" height="36" viewBox="0 0 52 36" fill="none" stroke="#c99ae6" stroke-width="1.5"><path d="M2 34V14L12 2h8L12 14h8v20zM30 34V14L40 2h8l-8 12h8v20z"/></svg>
  <p class="abs quote-copy">They transformed our online presence and helped us achieve remarkable results. Their team of professionals took the time to understand our brand and goals, and then crafted a stunning website that perfectly captured our essence. Not only did they deliver an exceptional design, but they also optimized it for search engines, resulting in a significant boost in organic traffic and improved visibility.</p>
  <div class="abs avatar" role="img" aria-label="Portrait photo of the client"></div>
  <div class="abs client">Arun Devika<small>Business owner at Tidewell</small></div>
  <svg class="abs" style="left:532px;top:3364px" width="80" height="14" viewBox="0 0 80 14" fill="none" stroke-width="1.5"><path d="M30 7H2M8 1 2 7l6 6" stroke="#2b2a35"/><path d="M48 7h28M70 1l6 6-6 6" stroke="#c77ff0"/></svg>
  <div class="abs tree-art" role="img" aria-label="Line drawing of a tree made of circuit traces"></div>
  <div class="abs" style="left:850px;top:3414px;width:350px;height:1px;background:var(--line)"></div>
</section>

<section class="contact">
  <h2 class="abs serif getintouch">LETS<br><span style="padding-left:80px">GET IN</span><br>TOUCH</h2>
  <div class="field" style="left:620px;top:3622px;width:485px">Full Name</div>
  <div class="field" style="left:620px;top:3685px;width:215px">Email</div>
  <div class="field" style="left:875px;top:3685px;width:230px">Phone</div>
  <div class="field" style="left:620px;top:3749px;width:485px">Message</div>
  <div class="btn" style="left:620px;top:3818px;width:126px;height:34px">Submit</div>
</section>

<footer class="abs footer">
  <div class="brand-name brand-name--footer">Loomtide</div>
  <div class="col" style="left:385px">
    <h4>NAVIGATION</h4>
    <ul><li>Services</li><li>Testimonials</li><li>Contact-Us</li><li>About-Us</li></ul>
  </div>
  <div class="col" style="left:627px">
    <h4>CONTACT</h4>
    <ul>
      <li><svg width="16" height="16" viewBox="0 0 16 16"><path d="M3 1h3l1.5 4-2 1.3a9 9 0 0 0 4.2 4.2L11 8.5l4 1.5v3a2 2 0 0 1-2 2A12 12 0 0 1 1 3a2 2 0 0 1 2-2z" fill="none" stroke="#fff" stroke-width="1.4"/></svg>+47 210 5583 46</li>
      <li><svg width="16" height="16" viewBox="0 0 16 16" fill="none" stroke="#fff" stroke-width="1.4"><rect x="1" y="3" width="14" height="10" rx="1"/><path d="m1 4 7 5 7-5"/></svg>info@loomtide.no</li>
      <li><svg width="16" height="16" viewBox="0 0 16 16" fill="none" stroke="#fff" stroke-width="1.4"><path d="M8 15s5-5 5-9A5 5 0 0 0 3 6c0 4 5 9 5 9z"/><circle cx="8" cy="6" r="1.8"/></svg>your address goes here</li>
    </ul>
    <div class="social"><i></i><i></i><i></i><i></i></div>
  </div>
  <div class="col" style="left:923px">
    <h4>QUICK LINKS</h4>
    <ul><li>Cookies</li><li>Security</li><li>Disclaimer</li><li>Compliance and Integrity</li></ul>
  </div>
</footer>
<div class="abs foot-rule"></div>
<div class="foot-bottom" style="left:80px">Terms and Conditions</div>
<div class="abs" style="left:268px;top:4326px;width:1px;height:34px;background:#8a7a88"></div>
<div class="foot-bottom" style="left:286px">Privacy Policy</div>
<div class="foot-bottom" style="right:82px">© 2023 loomtide. All rights reserved</div>

</body>
</html>
```